Website for Torvel Capital - investment banking firm

We have a corporate identity (thanks to Ranjita/41238) and want to extend that into a website design.  See the attached zipped files.
We have software folks in-house to do the coding.
See the attached Project Brief & Notes for more details.  Don't worry about the actual text - lorem ipsum will be fine.
The server will be Apache.
Thank you!
Desmond

```html
<!DOCTYPE html>
<html lang="en">
<head>
<meta charset="utf-8">
<title>Torvel Capital</title>
<link href="https://fonts.googleapis.com/css2?family=Lato:ital,wght@0,400;0,700;0,900;1,400&family=Tinos&family=Montserrat:wght@400;500&display=swap" rel="stylesheet">
<style>
:root{
  --blue:#1f4e8f;
  --blue-dark:#173f78;
  --blue-text:#2a5597;
  --ink:#1c1c1c;
  --grey:#7b7b7b;
  --line:#c9c9c9;
  --white:#ffffff;
  --badge:#e9e9e9;
}
*{box-sizing:border-box;margin:0;padding:0}
html,body{width:1200px;height:971px;overflow:hidden}
body{position:relative;font-family:'Lato',sans-serif;color:var(--ink);background:#f3f1ec}
.abs{position:absolute}

/* header */
.site-header{position:absolute;left:0;top:0;width:1200px;height:94px;background:linear-gradient(#f4f4f4,#e9e9e9);z-index:3}
.brand{left:132px;top:13px;height:66px;display:flex;align-items:center;gap:14px}
.brand-dot{width:54px;height:54px;border-radius:50%;background:var(--blue)}
.brand-rule{width:2px;height:66px;background:#9a9a9a}
.brand-name{font-family:'Lato',sans-serif;font-weight:700;font-size:32px;letter-spacing:1px;color:var(--blue-text)}
.top-contact{top:10px;display:flex;align-items:center;gap:6px;color:var(--blue-text);white-space:nowrap}
.top-contact.email{left:719px;font-size:11.5px;font-family:'Montserrat',sans-serif;font-weight:500}
.top-contact.phone{left:910px;font-size:19px;font-family:'Montserrat',sans-serif;font-weight:500}
.main-nav{left:498px;top:57px;display:flex;align-items:center;font-size:14px;color:var(--ink);white-space:nowrap}
.main-nav a{color:inherit;text-decoration:none;padding:0 12px;border-left:1px solid #b5b5b5;line-height:18px}
.main-nav a:first-child{border-left:none}
.main-nav a.active{background:var(--blue);color:var(--white);padding:5px 16px;line-height:17px;border-radius:2px}

/* hero */
.hero-photo{position:absolute;left:0;top:94px;width:1200px;height:732px;
  background:
   radial-gradient(ellipse 380px 260px at 420px 260px,#e7b248 0%,rgba(220,160,60,.6) 45%,rgba(0,0,0,0) 80%),
   radial-gradient(ellipse 300px 200px at 1000px 120px,#c99c62 0%,rgba(0,0,0,0) 80%),
   linear-gradient(160deg,#3a3a26 0%,#6c5a35 25%,#a07a3e 45%,#c89550 60%,#e3b979 78%,#f1d7a8 100%)}
.content-fade{position:absolute;left:0;top:568px;width:1200px;height:258px;background:linear-gradient(rgba(246,244,240,.78),rgba(246,244,240,.86))}
.hero-callout{left:606px;top:218px;width:463px;height:187px;background:rgba(246,246,246,.9);border-radius:3px;padding:8px 0 0 26px}
.hero-title{font-family:'Tinos',serif;font-size:34px;color:var(--blue-text);font-weight:400;line-height:1.1}
.hero-sub{font-family:'Montserrat',sans-serif;font-size:15px;color:var(--ink);margin-top:7px;font-weight:500}
.hero-sub.caps{font-size:17px;font-weight:500;margin-top:10px;letter-spacing:.2px}
.cta{left:633px;top:340px;height:47px;width:178px}
.cta span{position:absolute;left:15px;top:12px;color:var(--white);font-family:'Montserrat',sans-serif;font-size:18px}

/* feature cards */
.card{top:527px;width:288px;height:180px;border-radius:6px 6px 0 0;background:linear-gradient(rgba(255,255,255,.98) 0,rgba(250,250,250,.92) 40px,rgba(255,255,255,.55) 110px,rgba(255,255,255,0) 180px);box-shadow:0 -2px 4px rgba(0,0,0,.12)}
.card-head{position:absolute;left:14px;top:6px;display:flex;align-items:center;gap:12px;font-family:'Tinos',serif;font-weight:400;font-size:25px;color:var(--ink)}
.card-head .mark{width:28px;height:28px;border-radius:50%;background:var(--blue)}
.card-head em{font-style:normal;color:var(--blue-text)}
.card-icon{position:absolute;left:16px;top:53px;width:58px;height:58px;border:2px solid #2b2b2b;border-radius:50%;display:flex;align-items:center;justify-content:center}
.card-body{position:absolute;left:89px;top:52px;width:194px;font-size:13px;line-height:19.5px;letter-spacing:.45px}
.card-body ul{list-style:none}
.card-body li{position:relative;padding-left:14px;line-height:16px;margin-bottom:6px;letter-spacing:0}
.card-body li:before{content:"";position:absolute;left:1px;top:4px;border-left:5px solid #999;border-top:4px solid transparent;border-bottom:4px solid transparent}
.card-body h4{font-weight:700;font-size:13px;letter-spacing:0;line-height:18px}
.card-body p.news{letter-spacing:0;font-size:13px;line-height:19.5px}
.more{position:absolute;left:89px;top:145px;font-size:11px;font-weight:900;color:var(--blue-text);letter-spacing:.2px}

/* testimonials */
.divider{left:190px;top:705px;width:860px;height:1px;background:linear-gradient(90deg,rgba(160,160,160,0),#b9b9b9 20%,#b9b9b9 80%,rgba(160,160,160,0))}
.testi-label{left:130px;top:728px;width:138px;text-align:right;font-family:'Tinos',serif;font-size:26px;line-height:30px}
.testi-label .blue{color:var(--blue-text)}
.testi-quote{left:339px;top:733px;width:720px;font-style:italic;font-size:14px;line-height:20px;color:#222}
.testi-author{left:339px;top:781px;font-style:italic;font-size:14px;color:var(--blue-text)}

/* footer */
.site-footer{position:absolute;left:0;top:826px;width:1200px;height:145px;background:var(--blue);color:var(--white)}
.foot-h{position:absolute;top:23px;font-size:18px;font-weight:700}
.foot-rule{position:absolute;top:46px;height:1px;background:rgba(255,255,255,.35)}
.address{left:156px;top:55px;font-size:12.5px;line-height:19.6px}
.foot-contact{left:365px;font-size:13.5px;font-weight:700}
.newsletter{left:555px;top:60px;width:244px;height:28px;display:flex}
.newsletter .field{flex:1;background:var(--blue-dark);border:1px solid #2d5c9e;font-style:italic;font-size:12px;color:#b8c6dc;padding:6px 9px}
.newsletter .go{width:38px;background:#f2f2f2;color:var(--blue);font-weight:900;font-size:15px;text-align:center;line-height:28px}
.follow{left:554px;top:107px;font-size:15.5px;font-weight:700;display:flex;align-items:center;gap:10px}
.social{width:29px;height:29px;border:2px solid var(--white);border-radius:50%}
.foot-badge{left:916px;top:-28px;width:108px;height:108px;border-radius:50%;background:var(--badge);display:flex;align-items:center;justify-content:center;text-align:center;font-weight:700;font-size:15px;line-height:17px;color:var(--blue-text)}
.copyright{left:860px;top:84px;width:220px;text-align:center;font-size:13.5px;line-height:19.5px}
</style>
</head>
<body>

<header class="site-header">
  <div class="abs brand">
    <div class="brand-dot"></div>
    <div class="brand-rule"></div>
    <div class="brand-name">TORVEL CAPITAL</div>
  </div>
  <div class="abs top-contact email">
    <svg width="30" height="22" viewBox="0 0 30 22"><rect x="1" y="1" width="24" height="20" rx="3" fill="none" stroke="#333" stroke-width="1.5"/><path d="M25 8 L29 11 L25 14" fill="none" stroke="#333" stroke-width="1.5"/><rect x="6" y="6" width="14" height="10" fill="#333"/><path d="M6 6 L13 12 L20 6" fill="none" stroke="#fff" stroke-width="1.2"/></svg>
    info@torvelcapital.com
  </div>
  <div class="abs top-contact phone">
    <svg width="30" height="22" viewBox="0 0 30 22"><rect x="1" y="1" width="24" height="20" rx="3" fill="none" stroke="#333" stroke-width="1.5"/><path d="M25 8 L29 11 L25 14" fill="none" stroke="#333" stroke-width="1.5"/><rect x="9" y="4" width="8" height="14" rx="1.5" fill="#333"/><rect x="10.5" y="6" width="5" height="6" fill="#fff"/></svg>
    555-318-4470
  </div>
  <nav class="abs main-nav">
    <a class="active" href="#">About</a>
    <a href="#">Services</a>
    <a href="#">Current Engagements</a>
    <a href="#">Completed Transactions</a>
    <a href="#" style="border-left-color:#6b95c8">Contact Us</a>
  </nav>
</header>

<div class="hero-photo" role="img" aria-label="Photograph of a rowing crew in yellow vests pulling oars on sunlit water"></div>
<div class="content-fade"></div>

<section class="abs hero-callout">
  <h1 class="hero-title">Private Investment Banking</h1>
  <p class="hero-sub">advisory firm that acts as an intermediary on behalf of</p>
  <p class="hero-sub caps">BUYERS &amp; SELLERS OF PRIVATE COMPANIES.</p>
</section>
<a class="abs cta" href="#">
  <svg width="178" height="47" viewBox="0 0 178 47"><path d="M0 0 H160 L178 23.5 L160 47 H0 Z" fill="#1f4e8f"/></svg>
  <span>Get Started Now</span>
</a>

<article class="abs card" style="left:134px">
  <h2 class="card-head"><span class="mark"></span><span><em>Who</em> We Are</span></h2>
  <div class="card-icon"><svg width="30" height="30" viewBox="0 0 30 30"><circle cx="15" cy="9" r="6" fill="#2b2b2b"/><path d="M3 28 C4 19 9 16 15 16 C21 16 26 19 27 28 Z" fill="#2b2b2b"/></svg></div>
  <div class="card-body">Torvel Capital's history in mergers and acquisitions traces back to 1998. We pride our selves in successfully</div>
  <a class="more">READ MORE »</a>
</article>

<article class="abs card" style="left:456px">
  <h2 class="card-head"><span class="mark"></span><span><em>What</em> We Do</span></h2>
  <div class="card-icon"><svg width="34" height="34" viewBox="0 0 34 34"><circle cx="13" cy="20" r="8" fill="none" stroke="#2b2b2b" stroke-width="5" stroke-dasharray="3 2.2"/><circle cx="13" cy="20" r="5" fill="#2b2b2b"/><circle cx="13" cy="20" r="2" fill="#fff"/><circle cx="25" cy="9" r="5" fill="none" stroke="#2b2b2b" stroke-width="4" stroke-dasharray="2.4 1.8"/><circle cx="25" cy="9" r="1.5" fill="#fff"/></svg></div>
  <div class="card-body" style="top:55px">
    <ul>
      <li>Buy-Side Acquisitions</li>
      <li>Recapitalizations &amp; Growth Capital Partnerships</li>
      <li>Sell-Side Transactions</li>
    </ul>
  </div>
  <a class="more">READ MORE »</a>
</article>

<article class="abs card" style="left:778px">
  <h2 class="card-head"><span class="mark"></span><span><em>Latest</em> News</span></h2>
  <div class="card-icon"><svg width="32" height="30" viewBox="0 0 32 30"><rect x="3" y="10" width="6" height="9" fill="#2b2b2b"/><path d="M9 10 L22 3 V26 L9 19 Z" fill="#2b2b2b"/><rect x="24" y="11" width="4" height="7" rx="1.5" fill="#2b2b2b"/><path d="M7 19 L10 27 H14 L12 19 Z" fill="#2b2b2b"/></svg></div>
  <div class="card-body" style="top:53px">
    <h4>Kauitm veleum iriure lorrfu</h4>
    <p class="news">Hdrehrit in vulptate velit essehi molestie coequa. molestie uitmi veleum iriure lorrfu hdrehrit</p>
  </div>
  <a class="more">READ MORE »</a>
</article>

<div class="abs divider"></div>
<div class="abs testi-label"><span class="blue">Client</span><br>Testimonials</div>
<svg class="abs" style="left:290px;top:728px" width="24" height="58" viewBox="0 0 24 58"><path d="M0 0 L24 29 L0 58 Z" fill="#e2e0dc" opacity=".9"/></svg>
<p class="abs testi-quote"><svg width="24" height="18" viewBox="0 0 24 18" style="vertical-align:-2px"><path d="M2 18 V10 C2 4 5 1 10 0 L10 3 C7 4 6 6 6 8 H10 V18 Z M13 18 V10 C13 4 16 1 21 0 L21 3 C18 4 17 6 17 8 H21 V18 Z" fill="#a9a9a9"/></svg> Lorem ipsum sit amet consectet uradi incididunt ut labore et dolore magna aliquaps enimi ad minim veniam quiidunt ut labore etpvloore magn incididunt ut labore et dolore na aliquatmp enimt ad minim veniam quiidunt ut labore <svg width="24" height="18" viewBox="0 0 24 18" style="vertical-align:-8px"><path d="M22 0 V8 C22 14 19 17 14 18 L14 15 C17 14 18 12 18 10 H14 V0 Z M11 0 V8 C11 14 8 17 3 18 L3 15 C6 14 7 12 7 10 H3 V0 Z" fill="#a9a9a9"/></svg></p>
<p class="abs testi-author">Mr. Dolore na Aliqua</p>

<footer class="site-footer">
  <h3 class="foot-h" style="left:133px">Contact Info</h3>
  <div class="foot-rule" style="left:133px;width:366px"></div>
  <svg class="abs" style="left:134px;top:59px" width="11" height="15" viewBox="0 0 11 15"><path d="M5.5 0 C2.5 0 0 2.3 0 5.3 C0 9 5.5 15 5.5 15 C5.5 15 11 9 11 5.3 C11 2.3 8.5 0 5.5 0 Z" fill="#c9d4e4"/><circle cx="5.5" cy="5.3" r="2" fill="#1f4e8f"/></svg>
  <p class="abs address">Hong Kong: Room 1804<br>Harbourline Tower<br>12 - 18 Lockfield Road East<br>Kowloon Bay, Hong Kong</p>
  <svg class="abs" style="left:339px;top:56px" width="10" height="16" viewBox="0 0 10 16"><rect x="1" y="1" width="8" height="14" rx="1.5" fill="none" stroke="#c9d4e4" stroke-width="1.5"/><rect x="3" y="3" width="4" height="7" fill="#c9d4e4"/></svg>
  <p class="abs foot-contact" style="top:55px;font-size:15px">555-318-4470</p>
  <svg class="abs" style="left:337px;top:91px" width="15" height="11" viewBox="0 0 15 11"><rect x=".5" y=".5" width="14" height="10" fill="#c9d4e4"/><path d="M.5 .5 L7.5 6 L14.5 .5" fill="none" stroke="#1f4e8f"/></svg>
  <p class="abs foot-contact" style="top:88px">info@torvelcapital.com</p>

  <h3 class="foot-h" style="left:554px">Newsletter Signup</h3>
  <div class="foot-rule" style="left:554px;width:241px"></div>
  <div class="abs newsletter"><div class="field">Enter your email</div><div class="go">GO</div></div>
  <div class="abs follow">Follow Us On:
    <span class="social" aria-label="Social profile 1"></span>
    <span class="social" aria-label="Social profile 2"></span>
    <span class="social" aria-label="Social profile 3"></span>
    <span class="social" aria-label="Social profile 4"></span>
  </div>

  <div class="abs foot-badge">Torvel<br>Capital</div>
  <p class="abs copyright">© Copyright 2014 Torvel Capital.<br>All Rights Reserved</p>
</footer>

</body>
</html>
```